"On the Air" Sign for our podcast studio

We need a sign that says "TQRW <<logo>> is On The Air."

Would like this to be two color (black and red.) Ideally in an art deco style. We are going to use this sign on an interior wall to our studio to let people know when the studio is in use, so it should be noticeable right away.

The intention is to have this sign fabricated in a transparent material with the foreground in opaque black and the background in transparent red to show light through it, or we would consider a black opaque background with a red transparent design.

I've attached some examples to show purpose.

Target Market(s)

Fans of this websites - https://skylanemarketadvisors.example

Industry/Entity Type

Aviation industry

Font styles to use
Decorative

Colors
EB3D1F
EC4F4E
F09395
F8D3D4
FCEDEE

Requirements
Must have
• The included logo, and the words "On the Air."
Nice to have
• Art Deco style
Should not have
• Anything that could not be used in a transparent sign that lights up from behind.

```html
<!DOCTYPE html>
<html lang="en">
<head>
<meta charset="utf-8">
<title>TQRW On The Air Sign</title>
<link href="https://fonts.googleapis.com/css2?family=Federo&display=swap" rel="stylesheet">
<style>
  :root {
    --page: #ffffff;
    --panel: #0c0c0c;
    --panel-lit-center: #2f2f2f;
    --ink-flat: #c4282b;
    --ink-lit: #e3000f;
  }
  html, body {
    margin: 0;
    width: 1200px;
    height: 686px;
    overflow: hidden;
    background: var(--page);
  }
  .sign {
    position: absolute;
    width: 480px;
    height: 480px;
    box-shadow: 0 4px 14px rgba(0,0,0,0.45);
  }
  .sign--flat { left: 93px; top: 108px; background: var(--panel); }
  .sign--lit {
    left: 629px; top: 105px;
    background: radial-gradient(circle at 50% 62%, var(--panel-lit-center) 0%, #161616 45%, var(--panel) 80%);
  }
  .sign svg { display: block; width: 100%; height: 100%; }
  .sign--flat svg { --ink: var(--ink-flat); }
  .sign--lit svg { --ink: var(--ink-lit); }
  .frame line, .frame path { stroke: var(--ink); fill: none; }
  .headline, .brand-name { fill: var(--ink); font-family: "Federo", sans-serif; }
  .brand-dot { fill: var(--ink); }
</style>
</head>
<body>
  <svg width="0" height="0" style="position:absolute">
    <defs>
      <filter id="neon-glow" x="-20%" y="-20%" width="140%" height="140%">
        <feGaussianBlur in="SourceGraphic" stdDeviation="6" result="blur"/>
        <feMerge><feMergeNode in="blur"/><feMergeNode in="SourceGraphic"/></feMerge>
      </filter>
      <g id="sign-art">
        <g class="frame">
          <path d="M170 290 V233 A226 226 0 0 1 622 233 V290" stroke-width="5"/>
          <line x1="271" y1="48" x2="271" y2="78" stroke-width="5"/>
          <line x1="354" y1="14" x2="354" y2="78" stroke-width="5"/>
          <line x1="437" y1="14" x2="437" y2="78" stroke-width="5"/>
          <line x1="520" y1="48" x2="520" y2="78" stroke-width="5"/>
          <line x1="174" y1="192" x2="249" y2="192" stroke-width="5"/>
          <line x1="174" y1="239" x2="249" y2="239" stroke-width="5"/>
          <line x1="547" y1="192" x2="622" y2="192" stroke-width="5"/>
          <line x1="547" y1="239" x2="622" y2="239" stroke-width="5"/>
          <line x1="92" y1="290" x2="695" y2="290" stroke-width="9"/>
          <line x1="102" y1="712" x2="685" y2="712" stroke-width="9"/>
          <line x1="170" y1="712" x2="170" y2="787" stroke-width="5"/>
          <line x1="622" y1="712" x2="622" y2="787" stroke-width="5"/>
          <line x1="174" y1="756" x2="350" y2="756" stroke-width="5"/>
          <line x1="442" y1="756" x2="617" y2="756" stroke-width="5"/>
        </g>
        <g class="brand">
          <text class="brand-name" x="378" y="222" font-size="62" text-anchor="middle">TQRW</text>
          <circle class="brand-dot" cx="510" cy="185" r="13"/>
        </g>
        <text class="headline" x="173" y="488" font-size="232" textLength="432" lengthAdjust="spacingAndGlyphs">IS ON</text>
        <text class="headline" x="152" y="674" font-size="218" textLength="495" lengthAdjust="spacingAndGlyphs">THE AIR</text>
      </g>
    </defs>
  </svg>

  <div class="sign sign--flat">
    <svg viewBox="0 0 787 787" aria-label="TQRW is on the air sign, unlit">
      <use href="#sign-art"/>
    </svg>
  </div>

  <div class="sign sign--lit">
    <svg viewBox="0 0 787 787" aria-label="TQRW is on the air sign, lit">
      <g filter="url(#neon-glow)"><use href="#sign-art"/></g>
    </svg>
  </div>
</body>
</html>
```